Business Cards

I'm an contractor and consultant in IT Project management. I'd like a design for business cards.
In my work I mostly meet clients, peer project managers and technical staff. I usually exchange business cards at technical conventions or when networking.
I provide services that are:
- Updated, always with a fresh look on technology
- Solid and reliable
- Flexible schedule and always available
The current business card has been attached to provide information.
Target Market(s)
IT managers, IT project managers, consultants, recruitment staff. Age 30-45 years. College/University degree.
Industry/Entity Type
Contractor
Colors
Designer to choose colors to be used in the design.
Requirements
Must have
- Two sides, one side with personal information and the other side with company name.
Text in Norwegian, including Norwegian characters
Nice to have
- It should be possible for non-Norwegian speakers to read the contact details.

```html
<!DOCTYPE html>
<html lang="no">
<head>
<meta charset="utf-8">
<title>Brække Consulting AS – Visittkort</title>
<link rel="stylesheet" href="https://fonts.googleapis.com/css2?family=Tinos:wght@400;700&display=swap">
<style>
  :root {
    --page: #ffffff;
    --card: #ffffff;
    --card-edge: #8a8a8a;
    --band: #37494b;
    --ink: #111111;
    --ink-on-band: #ffffff;
    --ink-muted-on-band: #1c2526;
  }
  * { box-sizing: border-box; margin: 0; padding: 0; }
  html, body {
    width: 1200px; height: 313px; overflow: hidden;
    background: var(--page);
    font-family: "Tinos", "Times New Roman", serif;
    color: var(--ink);
  }
  .canvas { position: relative; width: 1200px; height: 313px; }
  .card {
    position: absolute; top: 0; height: 313px;
    background: var(--card);
    border: 1px solid var(--card-edge);
    overflow: hidden;
  }
  .card--contact { left: 0; width: 562px; }
  .card--company { left: 637px; width: 552px; }

  .company-name {
    position: absolute; left: 14px; top: 18px;
    font-size: 35px; font-variant: small-caps; line-height: 1;
    letter-spacing: 0.2px; white-space: nowrap;
  }
  .company-name .suffix { font-weight: 700; font-variant: normal; }
  .tagline {
    position: absolute; left: 14px; top: 69px;
    font-size: 23px; line-height: 1; white-space: nowrap;
  }
  .band { position: absolute; background: var(--band); }
  .card--contact .band--name { left: 280px; top: 106px; width: 282px; height: 102px; }
  .card--company .band--name { left: 0; top: 104px; width: 552px; height: 103px; }

  .person-name {
    position: absolute; font-size: 42px; font-variant: small-caps;
    line-height: 1; white-space: nowrap;
  }
  .person-role {
    position: absolute; font-size: 26px; line-height: 1; white-space: nowrap;
  }
  .card--contact .person-name { left: 10px; top: 14px; color: var(--ink-muted-on-band); }
  .card--contact .person-role { right: 10px; top: 64px; color: var(--ink-muted-on-band); }
  .card--company .person-name { right: 44px; top: 10px; color: var(--ink-on-band); }
  .card--company .person-role { right: 6px; top: 62px; color: var(--ink-on-band); }

  .address {
    position: absolute; left: 14px; top: 210px;
    font-size: 20px; line-height: 24px; font-style: normal;
  }
  .band--footer {
    left: 0; top: 282px; width: 562px; height: 31px;
    display: flex; justify-content: space-between; align-items: center;
    padding: 0 12px 0 14px; font-size: 20px; color: var(--ink);
  }
  .website {
    position: absolute; left: 0; width: 100%; top: 236px;
    text-align: center; font-size: 28px; line-height: 1;
  }
  .website-rule { position: absolute; left: 125px; top: 275px; }
</style>
</head>
<body>
<div class="canvas">
  <section class="card card--contact" aria-label="Kontaktside">
    <h1 class="company-name">Brække Consulting <span class="suffix">AS</span></h1>
    <p class="tagline">IT Implementering</p>
    <div class="band band--name">
      <p class="person-name">Ivar Brække</p>
      <p class="person-role">IT Rådgiver</p>
    </div>
    <address class="address">
      Vossegata 14<br>
      0475 Oslo<br>
      Mobil: 91234567
    </address>
    <div class="band band--footer">
      <span class="footer-web">www.braekkeconsulting.no</span>
      <span class="footer-mail">ivar@braekkeconsulting.no</span>
    </div>
  </section>

  <section class="card card--company" aria-label="Firmaside">
    <h2 class="company-name">Brække Consulting <span class="suffix">AS</span></h2>
    <p class="tagline">IT Implementering</p>
    <div class="band band--name">
      <p class="person-name">Ivar Brække</p>
      <p class="person-role">IT Rådgiver</p>
    </div>
    <p class="website">www.braekkeconsulting.no</p>
    <svg class="website-rule" width="298" height="2" aria-hidden="true">
      <rect width="298" height="2" fill="var(--band)"/>
    </svg>
  </section>
</div>
</body>
</html>
```